Oregon Pawnbroker About Us Brochure

We need to make a front/back tri-fold "about us" informative brochure using the bullet points uploaded. Our association represents licensed pawnbrokers in the state of Oregon and this will be distributed to the entire legislative body in our state. I have attached our logo, but feel free to be creative with logo to enhance the overall appearance of the brochure.

Target Market(s)

Regulators and Politicians

Industry/Entity Type

Pawnbroker

Requirements
Must have
• Professional Appearance
Nice to have
• Graphics, color scheme

```html
<!DOCTYPE html>
<html lang="en">
<head>
<meta charset="utf-8">
<title>Oregon Collateral Lenders Alliance – Tri-fold Brochure</title>
<link rel="stylesheet" href="https://fonts.googleapis.com/css2?family=Fira+Sans:wght@700;800;900&family=PT+Sans:wght@400;700&display=swap">
<style>
  :root {
    --navy: #2e2a7a;
    --orange: #ee7023;
    --sky: #cfe6f3;
    --grey: #dcdcdc;
    --ink: #1f1f2e;
    --white: #ffffff;
    --backdrop: #e9e6e1;
  }
  * { box-sizing: border-box; margin: 0; padding: 0; }
  html, body { width: 1200px; height: 927px; overflow: hidden; background: var(--backdrop); }
  body { position: relative; font-family: "PT Sans", sans-serif; color: var(--ink); }

  .sheet {
    position: absolute; top: 237px; width: 585px; height: 452px;
    background: var(--white); overflow: hidden;
    box-shadow: 0 6px 18px rgba(0,0,0,.18);
  }
  .sheet--inside { left: 5px; }
  .sheet--outside { left: 610px; }
  .sheet__art { position: absolute; inset: 0; width: 585px; height: 452px; }

  .panel { position: absolute; top: 0; width: 195px; height: 452px; }
  .panel--1 { left: 0; } .panel--2 { left: 195px; } .panel--3 { left: 390px; }

  .panel-title {
    position: absolute; font-family: "Fira Sans", sans-serif; font-weight: 800;
    color: var(--orange); text-align: center; line-height: 1.1; font-size: 14px;
  }
  .bullets { position: absolute; list-style: none; font-size: 7.6px; line-height: 1.28; }
  .bullets li { position: relative; padding-left: 10px; margin-bottom: 4px; }
  .bullets li::before {
    content: ""; position: absolute; left: 0; top: 3px; width: 4px; height: 4px;
    border-radius: 50%; background: var(--orange);
  }
  .bullets--light { color: var(--white); }
  .bullets--light li::before { background: var(--white); }
  .sublist { list-style: none; margin-top: 2px; }
  .sublist li { padding-left: 9px; margin-bottom: 1px; }
  .sublist li::before { border-radius: 0; width: 3px; height: 3px; background: var(--ink); }

  .web { position: absolute; font-size: 6.5px; color: var(--white); font-weight: 700; }

  .brand {
    position: absolute; display: flex; flex-direction: column; align-items: center; gap: 4px;
    font-family: "PT Sans", sans-serif; font-weight: 700; color: var(--navy);
    font-size: 7px; text-align: center; line-height: 1.1;
  }
  .brand__mark { width: 46px; height: 46px; border-radius: 50%; background: var(--white); border: 2px solid var(--grey); }

  .cover-title {
    position: absolute; left: 410px; top: 22px; width: 165px;
    font-family: "Fira Sans", sans-serif; font-weight: 900; color: var(--orange);
    font-size: 40px; line-height: .88; text-align: right;
  }
  .cover-sub {
    position: absolute; left: 410px; top: 100px; width: 165px; text-align: right;
    font-family: "Fira Sans", sans-serif; font-weight: 700; color: var(--navy); font-size: 10.5px;
  }
  .cover-sub span { font-family: "PT Sans", sans-serif; font-weight: 400; }
</style>
</head>
<body>

<!-- Inside spread -->
<section class="sheet sheet--inside" aria-label="Brochure inside spread">
  <svg class="sheet__art" viewBox="0 0 585 452" aria-hidden="true">
    <rect x="195" y="0" width="195" height="452" fill="var(--sky)"/>
    <rect x="0" y="0" width="390" height="96" fill="var(--navy)"/>
    <polygon points="0,96 150,96 175,62 195,96" fill="var(--white)"/>
    <polygon points="195,96 330,96 368,58 390,96" fill="var(--sky)"/>
    <polygon points="390,0 585,0 585,84 390,114" fill="var(--navy)"/>
    <polygon points="0,437 585,402 585,452 0,452" fill="var(--orange)"/>
  </svg>
  <div role="img" aria-label="Photo of hands holding a payment card over a laptop"
       style="position:absolute;left:0;top:330px;width:390px;height:100px;background:linear-gradient(180deg,rgba(207,230,243,0),#c7ccd3 40%,#a9b0ba);clip-path:polygon(0 10%,100% 0,100% 80%,0 100%);"></div>
  <div role="img" aria-label="Photo of two cheering business people outdoors"
       style="position:absolute;left:390px;top:215px;width:195px;height:190px;background:linear-gradient(160deg,#eef1f4,#b9c3cf 55%,#3c4f7a);"></div>

  <div class="panel panel--1">
    <h2 class="panel-title" style="left:0;top:34px;width:195px;">About Our<br>Industry</h2>
    <ul class="bullets" style="left:14px;top:108px;width:172px;">
      <li>Pawnbroking is the oldest form of regulated consumer credit.</li>
      <li>The Department of Consumer and Business Services issues the pawnbroker licenses here in Oregon.</li>
      <li>Currently, Oregon has 83 individually licensed pawnshops, 78 of which are brick-and-mortar, family-owned and operated businesses.</li>
      <li>Pawnbrokers offer highly regulated safety-net funds to consumers on a face-to-face basis from Main Street locations across the state.</li>
      <li>Lending decisions are solely based on the collateral and pawn transactions are non-recourse. No credit inquiries. No credit reporting. No collections. No cycle of debt.</li>
      <li>Pawnbrokers provide safe, secure storage for items customers cannot or do not want to store themselves, including oversized or seasonal items construction equipment, and firearms.</li>
    </ul>
  </div>

  <div class="panel panel--2">
    <h2 class="panel-title" style="left:0;top:52px;width:195px;">Regulation</h2>
    <ul class="bullets" style="left:14px;top:108px;width:172px;">
      <li>Pawnshops are heavily regulated and work closely with the federal, state and local governments and law enforcement.</li>
      <li>ORS 726 and OAR 441-740 define the requirements for our industry here in Oregon including the requirements of a loan, duration of a loan, as well as the interest and fees charged.</li>
      <li>Transactions require customer to present government issued photo identification.</li>
      <li>All transactions are reported daily to law enforcement.</li>
      <li>Oregon Pawnbrokers work closely with the following regulators:
        <ul class="sublist">
          <li>Department of Consumer and Business Services</li>
          <li>Bureau of Alcohol Tobacco and Firearms</li>
          <li>State Police</li>
          <li>Department of Agriculture</li>
        </ul>
      </li>
    </ul>
  </div>

  <div class="panel panel--3">
    <h2 class="panel-title" style="left:6px;top:20px;width:183px;font-size:13px;">Oregon Pawnbroker Statistics<br>(as reported by DCBS)</h2>
    <ul class="bullets" style="left:14px;top:126px;width:172px;">
      <li>Average loan amount in 2020 was $175</li>
      <li>Redemption rate of 72%</li>
      <li>Oregon pawnshops made approximately 206,500 loans in 2020, lending $33.2 million to Oregon customers.</li>
      <li>Police pickup rate of 0.085%</li>
    </ul>
    <p class="web" style="left:60px;top:418px;">www.collaterallendersalliance.org</p>
  </div>
</section>

<!-- Outside spread -->
<section class="sheet sheet--outside" aria-label="Brochure outside spread">
  <svg class="sheet__art" viewBox="0 0 585 452" aria-hidden="true">
    <polygon points="110,0 195,0 195,150" fill="var(--grey)"/>
    <rect x="195" y="0" width="195" height="452" fill="var(--navy)"/>
    <polygon points="195,0 390,0 390,190 292,300 195,150" fill="var(--orange)"/>
    <polygon points="390,0 585,0 585,200 390,200" fill="var(--white)"/>
  </svg>
  <div role="img" aria-label="Photo of glass skyscrapers against a blue sky"
       style="position:absolute;left:390px;top:200px;width:195px;height:252px;background:linear-gradient(180deg,#cfe1f3,#6f93c4 50%,#2f4f8c);"></div>
  <svg style="position:absolute;left:390px;top:200px;" width="195" height="252" viewBox="0 0 195 252" aria-hidden="true">
    <polygon points="0,0 40,0 0,252" fill="var(--navy)"/>
  </svg>

  <div class="panel panel--1">
    <h2 class="panel-title" style="left:14px;top:70px;width:170px;font-size:13px;">Why Pawnbrokers are Important to Oregon Consumers</h2>
    <ul class="bullets" style="left:16px;top:130px;width:168px;font-size:8px;">
      <li>Without state-licensed pawnbrokers, Oregonians could be forced to borrow from unlicensed people with unregulated loans that include very high interest rates or instead, forced to sell their property entirely, diminishing their personal assets.</li>
      <li>Other credit based lenders, such as banks and credit unions, do not offer Oregonians loan products at the small dollar amounts our industry serves.</li>
      <li>Pawnbrokers provide a same day financial solution.</li>
      <li>Pawnbrokers are invested in our communities and are sensitive to the needs of our customers.</li>
    </ul>
  </div>

  <div class="panel panel--2">
    <h2 class="panel-title" style="left:10px;top:28px;width:175px;color:var(--white);font-size:13px;">About the Oregon Collateral Lenders Alliance</h2>
    <ul class="bullets bullets--light" style="left:18px;top:90px;width:165px;font-size:8px;">
      <li>United voice of Oregon Pawnbrokers</li>
      <li>Represents majority of pawnbrokers, both number of licensees and transactions processed</li>
      <li>Single point of contact for Oregon Legislature and all regulators to communicate with our industry.</li>
    </ul>
    <div class="brand" style="left:37px;top:330px;width:120px;color:var(--white);">
      <span class="brand__mark"></span>
      <span>Oregon Collateral Lenders Alliance</span>
    </div>
    <p class="web" style="left:42px;top:420px;font-size:7px;">www.collaterallendersalliance.org</p>
  </div>

  <h1 class="cover-title">Quick<br>Facts</h1>
  <p class="cover-sub"><span>about</span> Oregon Pawnbrokers</p>
  <div class="brand" style="left:440px;top:122px;width:120px;">
    <span class="brand__mark"></span>
    <span>Oregon Collateral Lenders Alliance</span>
  </div>
</section>

</body>
</html>
```